automotive repair and collision repair shop card

our company is called K.R Motor service we are a automotive repair company
we also do government inspections. the company information is on the cards. I would like you to use my new logo and create a new card and use the information from my old card. Good Luck!!

Industry/Entity Type

Car Repair

Contact Information for Business Card

Address: #417-15862 91 Ave, Surrey, BC V5T 8K4
Phone:(604) 555-0187
fax 604 555 0142
website www.krmotor.example

Font styles to use
Serif
Sans Serif

Requirements
Must have
• all the information
Should not have
• the owner and there name

```html
<!DOCTYPE html>
<html lang="en">
<head>
<meta charset="utf-8">
<title>K.R Motor service – Business Card</title>
<link href="https://fonts.googleapis.com/css2?family=Oswald:wght@400&family=Arimo:wght@400;700&display=swap" rel="stylesheet">
<style>
  :root {
    --backdrop: #ebebeb;
    --card-dark: #1f1f1f;
    --card-light: #fbfbfb;
    --ink: #2b2b2b;
    --ink-soft: #555555;
    --rule: #9a9a9a;
    --on-dark: #f2f2f2;
  }
  html, body {
    margin: 0;
    width: 1200px;
    height: 800px;
    overflow: hidden;
    background: var(--backdrop);
  }
  .canvas {
    position: relative;
    width: 1200px;
    height: 800px;
  }
  .card {
    position: absolute;
    top: 257px;
    width: 500px;
    height: 286px;
    box-shadow: 0 2px 6px rgba(0,0,0,0.12);
    box-sizing: border-box;
  }
  .card--front {
    left: 70px;
    background: var(--card-dark);
    display: flex;
    align-items: center;
    justify-content: center;
  }
  .card--back {
    left: 630px;
    background: var(--card-light);
    color: var(--ink);
    font-family: "Arimo", Arial, sans-serif;
  }
  .wordmark {
    display: flex;
    align-items: center;
    gap: 10px;
    font-family: "Oswald", "Arial Narrow", sans-serif;
    font-weight: 400;
    text-transform: uppercase;
    letter-spacing: 0.5px;
  }
  .wordmark__dot {
    border-radius: 50%;
  }
  .card--front .wordmark {
    color: var(--on-dark);
    font-size: 30px;
  }
  .card--front .wordmark__dot {
    width: 14px;
    height: 14px;
    background: var(--on-dark);
  }
  .card--back .wordmark {
    position: absolute;
    top: 38px;
    right: 34px;
    color: var(--ink);
    font-size: 20px;
  }
  .card--back .wordmark__dot {
    width: 10px;
    height: 10px;
    background: var(--ink);
  }
  .services {
    position: absolute;
    top: 96px;
    left: 356px;
    margin: 0;
    padding: 0;
    list-style: none;
    font-size: 9.5px;
    line-height: 12.5px;
    color: var(--ink-soft);
  }
  .services li::before {
    content: "•";
    margin-right: 4px;
    color: var(--ink);
  }
  .divider {
    position: absolute;
    top: 168px;
    left: 30px;
    width: 300px;
    height: 1px;
    background: var(--rule);
  }
  .contact {
    position: absolute;
    left: 30px;
    top: 190px;
    margin: 0;
    font-size: 10.5px;
    line-height: 15px;
    color: var(--ink-soft);
  }
  .contact__row {
    display: flex;
    gap: 6px;
  }
  .contact dt {
    font-weight: 700;
    color: var(--ink);
    width: 9px;
  }
  .contact dd {
    margin: 0;
  }
</style>
</head>
<body>
<main class="canvas">
  <section class="card card--front" aria-label="Card front">
    <div class="wordmark">
      <span class="wordmark__dot"></span>
      <span class="wordmark__name">K.R Motor service</span>
    </div>
  </section>

  <section class="card card--back" aria-label="Card back">
    <div class="wordmark">
      <span class="wordmark__dot"></span>
      <span class="wordmark__name">K.R Motor service</span>
    </div>

    <ul class="services">
      <li>Oil change</li>
      <li>Scheduled maintenance</li>
      <li>Body Work</li>
      <li>Paint</li>
      <li>Glass Replacement</li>
      <li>NWIC Claims</li>
      <li>Inspections</li>
      <li>Engine repair</li>
    </ul>

    <div class="divider"></div>

    <dl class="contact">
      <div class="contact__row"><dt>A</dt><dd>#417-15862 91 Ave, Surrey, BC V5T 8K4</dd></div>
      <div class="contact__row"><dt>P</dt><dd>(604) 555-0187</dd></div>
      <div class="contact__row"><dt>F</dt><dd>604 555 0142</dd></div>
      <div class="contact__row"><dt>W</dt><dd>www.krmotor.example</dd></div>
    </dl>
  </section>
</main>
</body>
</html>
```